Capability Statement Document/Flyer

Take the existing words from the capability statement document (attached) and design a unique folder/flyer document for professional use. Maybe something like a trifold or bifold style. Use approved colours and logo as per the attached files.
Our company designs and builds small onshore gas processing plants.

```html
<!DOCTYPE html>
<html lang="en">
<head>
<meta charset="utf-8">
<title>Clarivo Capability Statement</title>
<link href="https://fonts.googleapis.com/css2?family=Roboto:wght@300;400;500;700&display=swap" rel="stylesheet">
<style>
:root{
  --green:#1a6b55;
  --green-dark:#12594a;
  --green-pale:#eef3f0;
  --row-alt:#f3f8f6;
  --hill:#bfbfbf;
  --text:#6a6a6a;
  --ink:#151515;
  --board:#242424;
  --white:#ffffff;
  --black:#000000;
}
*{box-sizing:border-box;margin:0;padding:0}
html,body{width:875px;height:1200px;overflow:hidden}
body{background:var(--board);font-family:"Roboto",Arial,sans-serif;position:relative}
.page{position:absolute;height:527px;overflow:hidden;background:var(--white)}
.page--back{left:30px;top:28px;width:407px;background:var(--green)}
.page--cover{left:437px;top:28px;width:408px;background:var(--black)}
.page--about{left:30px;top:578px;width:407px}
.page--services{left:437px;top:578px;width:406px}

/* footer */
.footer{position:absolute;left:0;bottom:0;width:100%;height:60px}
.footer svg{position:absolute;inset:0;width:100%;height:100%}
.contact{position:absolute;top:27px;display:flex;align-items:center;gap:5px;color:var(--white);font-size:6.4px;line-height:9.5px}
.contact svg{position:static;width:11px;height:11px;flex:none}
.contact--address{left:14px}
.contact--mail{left:104px}
.contact--phone{left:206px}
.footer-name{position:absolute;right:12px;top:33px;width:76px;height:20px;border:1.5px solid var(--ink);color:var(--ink);font-weight:500;font-size:13px;letter-spacing:.5px;display:flex;align-items:center;justify-content:center}

/* back page */
.back-photo{position:absolute;left:0;top:0;width:100%;height:392px;background:linear-gradient(180deg,#8d92dc 0%,#c98dc6 22%,#4a5a7e 40%,#8f93ad 58%,#4f7f78 76%,var(--green) 100%)}
.back-name{position:absolute;left:123px;top:379px;width:163px;height:41px;border:2.5px solid var(--white);color:var(--white);font-size:28px;font-weight:500;letter-spacing:1px;display:flex;align-items:center;justify-content:center}
.back-band{position:absolute;left:0;top:434px;width:100%;height:60px;background:var(--white)}
.thanks{position:absolute;left:0;top:436px;width:100%;text-align:center;font-size:40px;font-weight:700;color:var(--green);letter-spacing:-.5px}

/* cover */
.cover-name{position:absolute;left:18px;top:14px;width:163px;height:41px;border:2.5px solid #9a9a9a;color:var(--green);font-size:28px;font-weight:700;letter-spacing:1px;display:flex;align-items:center;justify-content:center}
.cover-art{position:absolute;left:0;top:0;width:408px;height:400px}
.cover-title{position:absolute;left:0;top:380px;width:100%;text-align:center;font-size:29px;font-weight:500}
.cover-title .lead{color:var(--green)}
.cover-title .tail{color:#d0d0d0}
.cover-sub{position:absolute;left:0;top:427px;width:100%;text-align:center;color:var(--white);font-size:18px;font-weight:400;line-height:23px}

/* about page */
.section-bar{position:absolute;left:0;width:4px;height:26px;background:var(--green)}
.heading{position:absolute;left:20px;font-size:20px;font-weight:300;color:#8a8a8a;white-space:nowrap}
.heading strong{font-weight:700;color:var(--green)}
.body-copy{position:absolute;left:22px;width:360px;font-size:9.6px;line-height:12.8px;color:var(--text);font-weight:400;text-align:justify}
.vision{position:absolute;left:22px;top:108px;width:360px;height:49px;border:2px solid #cfcfcf;padding:4px 8px}
.vision-lead{font-size:12px;color:var(--text);line-height:18px}
.vision-line{font-size:13px;font-weight:700;color:var(--green);letter-spacing:.2px;line-height:19px}

.org{position:absolute;left:20px;top:281px;width:198px;height:122px}
.org-row{position:absolute;left:0;width:198px;height:37px;background:var(--green-pale);border-radius:3px}
.org-icon{position:absolute;left:5px;top:8px;width:20px;height:20px;border-radius:50%;background:var(--white);border:1px solid #d5ddd9}
.org-label{position:absolute;left:26px;top:6px;width:60px;font-size:4px;line-height:4.6px;color:#555}
.org-label b{display:block;font-size:4.6px;color:var(--ink);margin-bottom:1px}
.org-box{position:absolute;background:var(--green-dark);color:var(--white);font-size:4.2px;font-weight:700;display:flex;flex-direction:column;align-items:center;justify-content:flex-end;padding-bottom:3px;border-radius:2px;box-shadow:0 1px 2px rgba(0,0,0,.35)}
.org-box::before{content:"";width:6px;height:6px;border:1px solid var(--white);border-radius:50%;margin-bottom:3px}
.org-lines{position:absolute;left:0;top:0;width:198px;height:122px}

.principles-title{position:absolute;left:235px;top:309px;font-size:13.5px;font-weight:700;color:var(--green)}
.principles{position:absolute;left:240px;top:334px;width:165px;list-style:none}
.principles li{position:relative;padding-left:12px;font-size:10px;line-height:14.4px;color:var(--text)}
.principles svg{position:absolute;left:0;top:3px;width:8.5px;height:8.5px}
.objective-title{position:absolute;left:21px;top:419px;font-size:13.5px;font-weight:700;color:var(--green)}
.objective{position:absolute;left:21px;top:443px;width:340px;font-size:10px;line-height:14.5px;color:var(--text)}

/* services */
.section-rule{position:absolute;left:1px;top:18px;width:2px;height:26px;background:var(--green)}
.services{position:absolute;left:21px;top:61px;width:348px;border-collapse:collapse;box-shadow:0 3px 8px rgba(0,0,0,.18);border-radius:4px;overflow:hidden}
.services th{background:var(--green-dark);color:var(--white);font-size:9px;font-weight:500;height:23px}
.services td{height:32.1px;border-bottom:1px solid #dde7e3;vertical-align:middle}
.services tr:nth-child(even) td{background:var(--row-alt)}
.services .num{width:29px;background:var(--green-dark)!important;color:var(--white);text-align:center;font-size:12px;font-weight:500;border-bottom:1px solid #2c7a66}
.services .fn{width:111px;border-right:1px solid #dde7e3}
.fn-inner{display:flex;align-items:center;gap:8px;padding-left:9px;font-size:8.6px;font-weight:700;color:var(--ink);line-height:10px}
.fn-inner svg{width:17px;height:17px;flex:none}
.services .svc{padding-left:12px;font-size:8.2px;line-height:10.8px;color:var(--ink)}
</style>
</head>
<body>

<svg width="0" height="0" style="position:absolute" aria-hidden="true">
  <defs>
    <symbol id="i-pin" viewBox="0 0 24 24"><path d="M12 2a7 7 0 0 0-7 7c0 5 7 13 7 13s7-8 7-13a7 7 0 0 0-7-7zm0 10a3 3 0 1 1 0-6 3 3 0 0 1 0 6z" fill="#fff"/></symbol>
    <symbol id="i-send" viewBox="0 0 24 24"><path d="M2 11 22 3 15 21 11 14 2 11zm9 3 5-6" fill="#fff" stroke="#fff" stroke-width="1"/></symbol>
    <symbol id="i-phone" viewBox="0 0 24 24"><path d="M6 3l3 1 1 4-2 2c1 2 3 4 5 5l2-2 4 1 1 3-2 3C10 20 4 14 3 6z" fill="#fff"/><path d="M14 3a7 7 0 0 1 7 7M14 6a4 4 0 0 1 4 4" stroke="#fff" stroke-width="1.6" fill="none"/></symbol>
    <symbol id="i-tick" viewBox="0 0 24 24"><circle cx="12" cy="12" r="10" fill="none" stroke="#1a6b55" stroke-width="2"/><path d="M7 12l3.5 3.5L17 9" fill="none" stroke="#1a6b55" stroke-width="2"/></symbol>
    <symbol id="f-pm" viewBox="0 0 24 24"><rect x="4" y="3" width="14" height="19" rx="1" fill="none" stroke="#1b4f45" stroke-width="1.8"/><path d="M7 8h8M7 12h8M7 16h5" stroke="#1b4f45" stroke-width="1.6"/><circle cx="18" cy="19" r="4" fill="#1a6b55"/></symbol>
    <symbol id="f-eng" viewBox="0 0 24 24"><circle cx="12" cy="12" r="7" fill="none" stroke="#1b4f45" stroke-width="4" stroke-dasharray="3 2.5"/><circle cx="12" cy="12" r="5.5" fill="#1b4f45"/><circle cx="12" cy="12" r="2.5" fill="#fff"/></symbol>
    <symbol id="f-cart" viewBox="0 0 24 24"><path d="M2 4h3l3 11h11l2-8H6.5" fill="none" stroke="#1b4f45" stroke-width="1.8"/><circle cx="9" cy="19" r="1.7" fill="#1b4f45"/><circle cx="17" cy="19" r="1.7" fill="#1b4f45"/></symbol>
    <symbol id="f-doc" viewBox="0 0 24 24"><path d="M5 2h9l5 5v15H5z" fill="none" stroke="#1b4f45" stroke-width="1.8"/><path d="M8 10h8M8 14h5" stroke="#1b4f45" stroke-width="1.6"/><circle cx="17" cy="19" r="4" fill="#1a6b55"/></symbol>
    <symbol id="f-calc" viewBox="0 0 24 24"><rect x="5" y="2" width="14" height="20" rx="2" fill="#1b4f45"/><rect x="7" y="4" width="10" height="4" fill="#fff"/><path d="M8 11h2v2H8zm3 0h2v2h-2zm3 0h2v2h-2zM8 15h2v2H8zm3 0h2v2h-2zm3 0h2v2h-2z" fill="#fff"/></symbol>
    <symbol id="f-cal" viewBox="0 0 24 24"><rect x="3" y="4" width="18" height="17" rx="1.5" fill="none" stroke="#1b4f45" stroke-width="1.8"/><path d="M3 9h18M8 2v4M16 2v4" stroke="#1b4f45" stroke-width="1.8"/><path d="M6 12h3v2H6zm5 0h3v2h-3zm5 0h2v2h-2zM6 16h3v2H6zm5 0h3v2h-3z" fill="#1b4f45"/></symbol>
    <symbol id="f-shield" viewBox="0 0 24 24"><path d="M12 2 20 5v6c0 6-4 9-8 11-4-2-8-5-8-11V5z" fill="#1b4f45"/><path d="M12 7v6M12 15.5v1.5" stroke="#fff" stroke-width="2"/></symbol>
    <symbol id="f-gov" viewBox="0 0 24 24"><path d="M2 8 12 3l10 5z" fill="#1b4f45"/><path d="M5 10v8M9.5 10v8M14.5 10v8M19 10v8" stroke="#1b4f45" stroke-width="2.2"/><path d="M2 20h20" stroke="#1b4f45" stroke-width="2.2"/></symbol>
    <symbol id="f-crane" viewBox="0 0 24 24"><path d="M6 22V4M2 5h20M6 4l-3 1M6 8l4-3M18 5v7" stroke="#1b4f45" stroke-width="2" fill="none"/><rect x="16" y="12" width="4" height="3" fill="#1b4f45"/><path d="M3 22h7" stroke="#1b4f45" stroke-width="2"/></symbol>
    <symbol id="f-power" viewBox="0 0 24 24"><path d="M7 6.5a8 8 0 1 0 10 0" fill="none" stroke="#1b4f45" stroke-width="2"/><path d="M12 2v9" stroke="#1b4f45" stroke-width="2"/></symbol>
    <symbol id="f-team" viewBox="0 0 24 24"><circle cx="12" cy="7" r="3.2" fill="#1b4f45"/><circle cx="5" cy="9" r="2.5" fill="#1b4f45"/><circle cx="19" cy="9" r="2.5" fill="#1b4f45"/><path d="M6.5 19a5.5 5.5 0 0 1 11 0zM0.5 19a4.5 4.5 0 0 1 6-4.2A7 7 0 0 0 5.5 19zM23.5 19a4.5 4.5 0 0 0-6-4.2 7 7 0 0 1 1 4.2z" fill="#1b4f45"/></symbol>
    <symbol id="f-wrench" viewBox="0 0 24 24"><path d="M20 4a5 5 0 0 0-6.5 6L3 20.5 5.5 23 16 12.5A5 5 0 0 0 22 6l-3 3-3-1-1-3z" fill="#1b4f45" transform="translate(-1,-1)"/></symbol>
  </defs>
</svg>

<!-- Back page -->
<section class="page page--back">
  <div class="back-photo" role="img" aria-label="Photograph of a gas processing plant with storage tanks at dusk"></div>
  <div class="back-name">CLARIVO</div>
  <div class="back-band"></div>
  <div class="thanks">Thank You</div>
  <footer class="footer">
    <svg viewBox="0 0 407 60" preserveAspectRatio="none" aria-hidden="true">
      <rect x="0" y="0" width="407" height="60" fill="#ffffff" opacity="0"/>
      <path d="M288 60 L337 19 C352 4 382 -2 407 14 L407 60 Z" fill="var(--hill)"/>
      <path d="M0 19 H325 L278 60 H0 Z" fill="var(--green)"/>
    </svg>
    <div class="contact contact--address"><svg><use href="#i-pin"/></svg><span>Street Address Here<br>Singapore, 2222</span></div>
    <div class="contact contact--mail"><svg><use href="#i-send"/></svg><span>urname@email.com<br>www.websitename.com</span></div>
    <div class="contact contact--phone"><svg><use href="#i-phone"/></svg><span>+61 2 5550 0148<br>+61 2 5550 0148</span></div>
  </footer>
</section>

<!-- Cover -->
<section class="page page--cover">
  <svg class="cover-art" viewBox="0 0 408 400" aria-hidden="true">
    <circle cx="418" cy="160" r="236" fill="var(--green)"/>
    <circle cx="418" cy="160" r="229" fill="#b89470"/>
    <circle cx="143" cy="243" r="128" fill="var(--black)"/>
  </svg>
  <div role="img" aria-label="Photograph of a refinery under a golden evening sky" style="position:absolute;left:170px;top:-69px;width:458px;height:458px;border-radius:50%;background:linear-gradient(160deg,#e9c08a 0%,#c98a55 30%,#6f6a6a 60%,#3a4650 100%);clip-path:circle(50%);z-index:0;mask:none;display:none"></div>
  <div role="img" aria-label="Photograph of a refinery under a golden evening sky" style="position:absolute;left:0;top:0;width:408px;height:400px;clip-path:path('M 189 0 L 408 0 L 408 389 A 229 229 0 0 1 229 337 A 128 128 0 0 0 214 137 A 229 229 0 0 1 189 0 Z');background:linear-gradient(160deg,#f0c98f 0%,#d6955a 30%,#7d7472 58%,#3d4a55 100%)"></div>
  <div role="img" aria-label="Photograph of a field technician in hard hat inspecting yellow pipework with a tablet" style="position:absolute;left:24px;top:124px;width:238px;height:238px;border-radius:50%;background:radial-gradient(circle at 35% 40%,#e8b62c 0%,#9c7a2a 40%,#3b3a3c 75%,#1e2030 100%)"></div>
  <div class="cover-name">CLARIVO</div>
  <h1 class="cover-title"><span class="lead">Capability</span> <span class="tail">Statement</span></h1>
  <p class="cover-sub">Simplify Project Execution,<br>Streamline Operations</p>
  <footer class="footer">
    <svg viewBox="0 0 408 60" preserveAspectRatio="none" aria-hidden="true">
      <path d="M288 60 L337 19 C352 4 382 -2 408 14 L408 60 Z" fill="var(--hill)"/>
      <path d="M0 19 H325 L278 60 H0 Z" fill="var(--green)"/>
    </svg>
    <div class="contact contact--address"><svg><use href="#i-pin"/></svg><span>Street Address Here<br>Singapore, 2222</span></div>
    <div class="contact contact--mail"><svg><use href="#i-send"/></svg><span>urname@email.com<br>www.websitename.com</span></div>
    <div class="contact contact--phone"><svg><use href="#i-phone"/></svg><span>+61 2 5550 0148<br>+61 2 5550 0148</span></div>
  </footer>
</section>

<!-- About -->
<section class="page page--about">
  <div class="section-bar" style="top:18px"></div>
  <h2 class="heading" style="top:17px">Who are <strong>Clarivo?</strong></h2>
  <p class="body-copy" style="top:47px">Clarivo are a highly experienced team of Executive, Project, Construction, Commissioning and Operations specialists who combine deep technical knowledge with proven leadership to deliver unique Project Delivery Partner services to organisations in Australia.</p>
  <div class="vision">
    <p class="vision-lead">Our vision is straightforward:</p>
    <p class="vision-line">Simplify Project Execution, Streamline Operations.</p>
  </div>
  <div class="section-bar" style="top:168px"></div>
  <h2 class="heading" style="top:167px">What is a&nbsp; <strong>Project Delivery Partner?</strong></h2>
  <p class="body-copy" style="top:198px;text-align:left">A Project Delivery Partner (PDP) provides integrated project management along with technical, commercial and delivery support services to help an organisation successfully deliver a project. The PDP acts as the owner’s team while the owner retains accountability and key decision-making authority.</p>

  <div class="org">
    <div class="org-row" style="top:0">
      <div class="org-icon"></div>
      <p class="org-label"><b>OWNER</b>Provides project vision and strategic direction.</p>
    </div>
    <div class="org-row" style="top:42px">
      <div class="org-icon"></div>
      <p class="org-label"><b>PROJECT DELIVERY PARTNER</b>Manages and integrates the project delivery across all workstreams.</p>
    </div>
    <div class="org-row" style="top:85px">
      <div class="org-icon"></div>
      <p class="org-label"><b>CONTRACTORS</b>Deliver specialized services and execute project components.</p>
    </div>
    <svg class="org-lines" viewBox="0 0 198 122" aria-hidden="true">
      <path d="M117 33V46M117 75V85M83 85H169M83 85V91M126 85V91M169 85V91" stroke="#3f8a3a" stroke-width=".8" fill="none"/>
    </svg>
    <div class="org-box" style="left:93px;top:3px;width:50px;height:30px">Operator<br>XYZ</div>
    <div class="org-box" style="left:93px;top:46px;width:50px;height:29px">Clarivo</div>
    <div class="org-box" style="left:65px;top:91px;width:36px;height:28px">Engineering</div>
    <div class="org-box" style="left:108px;top:91px;width:36px;height:28px">Suppliers</div>
    <div class="org-box" style="left:151px;top:91px;width:34px;height:28px">Execution</div>
  </div>

  <h3 class="principles-title">PDP Core Principles:</h3>
  <ul class="principles">
    <li><svg><use href="#i-tick"/></svg>Owner controls the project</li>
    <li><svg><use href="#i-tick"/></svg>PDP enables delivery &amp; provides assurance</li>
    <li><svg><use href="#i-tick"/></svg>Contractors execute the work</li>
  </ul>
  <h3 class="objective-title">PDP Objective:</h3>
  <p class="objective">Deliver the project safely, on schedule, within budget and ready for operations; providing owner capability throughout the project lifecycle.</p>

  <footer class="footer">
    <svg viewBox="0 0 407 60" preserveAspectRatio="none" aria-hidden="true">
      <path d="M288 60 L337 19 C352 4 382 -2 407 14 L407 60 Z" fill="var(--hill)"/>
      <path d="M0 19 H325 L278 60 H0 Z" fill="var(--green)"/>
    </svg>
    <div class="contact contact--address"><svg><use href="#i-pin"/></svg><span>Street Address Here<br>Singapore, 2222</span></div>
    <div class="contact contact--mail"><svg><use href="#i-send"/></svg><span>urname@email.com<br>www.websitename.com</span></div>
    <div class="contact contact--phone"><svg><use href="#i-phone"/></svg><span>+61 2 5550 0148<br>+61 2 5550 0148</span></div>
    <div class="footer-name">CLARIVO</div>
  </footer>
</section>

<!-- Services -->
<section class="page page--services">
  <div class="section-rule"></div>
  <h2 class="heading" style="left:18px;top:17px">PDP <strong>Services</strong></h2>
  <table class="services">
    <thead><tr><th>#</th><th>Function</th><th>Clarivo Service</th></tr></thead>
    <tbody>
      <tr><td class="num">1</td><td class="fn"><div class="fn-inner"><svg><use href="#f-pm"/></svg>Project<br>Management</div></td><td class="svc">Planning, Reporting &amp; Delivery Leadership<br>from Concept to Completion</td></tr>
      <tr><td class="num">2</td><td class="fn"><div class="fn-inner"><svg><use href="#f-eng"/></svg>Engineering</div></td><td class="svc">Concept Selection, Design Coordination,<br>Technical Assurance &amp; Value Engineering</td></tr>
      <tr><td class="num">3</td><td class="fn"><div class="fn-inner"><svg><use href="#f-cart"/></svg>Procurement</div></td><td class="svc">Contracting Strategy, Tender Process &amp;<br>Supplier/Contractor Management</td></tr>
      <tr><td class="num">4</td><td class="fn"><div class="fn-inner"><svg><use href="#f-doc"/></svg>Approvals</div></td><td class="svc">Land Access, Regulator Engagement, Safety<br>Case, Permits &amp; Licenses</td></tr>
      <tr><td class="num">5</td><td class="fn"><div class="fn-inner"><svg><use href="#f-calc"/></svg>Cost Control</div></td><td class="svc">Budget Development, Forecasting &amp;<br>Management</td></tr>
      <tr><td class="num">6</td><td class="fn"><div class="fn-inner"><svg><use href="#f-cal"/></svg>Scheduling</div></td><td class="svc">Master Schedule Development, WBS,<br>Resource Allocation, Monitoring &amp; Updating</td></tr>
      <tr><td class="num">7</td><td class="fn"><div class="fn-inner"><svg><use href="#f-shield"/></svg>Risk Management</div></td><td class="svc">Risk Register, Identification, Mitigation &amp;<br>Reporting</td></tr>
      <tr><td class="num">8</td><td class="fn"><div class="fn-inner"><svg><use href="#f-gov"/></svg>Governance</div></td><td class="svc">Framework, Stage Gates, Change control,<br>Reporting &amp; Decision Support</td></tr>
      <tr><td class="num">9</td><td class="fn"><div class="fn-inner"><svg><use href="#f-crane"/></svg>Construction</div></td><td class="svc">Management &amp; Coordination of Contractor<br>Execution Teams</td></tr>
      <tr><td class="num">10</td><td class="fn"><div class="fn-inner"><svg><use href="#f-power"/></svg>Commissioning &amp;<br>Start-up</div></td><td class="svc">Lead Commissioning &amp; Start-up,<br>Completions System, Bring the Facility to<br>Steady-State</td></tr>
      <tr><td class="num">11</td><td class="fn"><div class="fn-inner"><svg><use href="#f-team"/></svg>Operations Readiness</div></td><td class="svc">People &amp; Organisation, Process &amp;<br>Procedures, Systems &amp; Technology</td></tr>
      <tr><td class="num">12</td><td class="fn"><div class="fn-inner"><svg><use href="#f-wrench"/></svg>Operations &amp;<br>Maintenance</div></td><td class="svc">Monitor &amp; Operate Asset, Minimize<br>Downtime, Lowest Possible OPEX for Owner</td></tr>
    </tbody>
  </table>
  <footer class="footer">
    <svg viewBox="0 0 406 60" preserveAspectRatio="none" aria-hidden="true">
      <path d="M287 60 L336 19 C351 4 381 -2 406 14 L406 60 Z" fill="var(--hill)"/>
      <path d="M0 19 H324 L277 60 H0 Z" fill="var(--green)"/>
    </svg>
    <div class="contact contact--address"><svg><use href="#i-pin"/></svg><span>Street Address Here<br>Singapore, 2222</span></div>
    <div class="contact contact--mail"><svg><use href="#i-send"/></svg><span>urname@email.com<br>www.websitename.com</span></div>
    <div class="contact contact--phone"><svg><use href="#i-phone"/></svg><span>+61 2 5550 0148<br>+61 2 5550 0148</span></div>
    <div class="footer-name">CLARIVO</div>
  </footer>
</section>

</body>
</html>
```